CAMPO DORMIDO

Campo Dormido is a tribute to the hidden treasures of Chile’s majestic mountain landscapes. Each bottle captures the essence of the Andes, where rugged peaks and fertile valleys create the perfect harmony for winemaking. With a label inspired by the mystique of the mountains, Campo Dormido invites you to uncover the rich flavors and stories hidden within its depths—a wine as bold and timeless as the land it comes from. the current design is old and not attractiv at all we want something new

Please create a mysterious, enigmatic label based on the typography and logo attached to the project. We need at least, at the entry level, five varietal products such as Carménère, Cabernet Sauvignon, Merlot, Chardonnay, and Malbec. Later, we would like to add more premium products, like a Reserva, a Special Reserva, or a Limited Edition. The design should be flexible and easily adaptable to accommodate various products while maintaining the same overall aesthetic.

Project Brief – Large-Scale Brand Label Design
We are developing a new large-scale brand with a structured range of wines. Below are the key design elements and specifications for the labels:

Entry-Level Wines (Bordeaux Bottle Shape)
Varietals: Cabernet Sauvignon, Carménère, Merlot, Cabernet-Merlot, Sauvignon Blanc.
Do not mention the word "varietals" on the label.
Next Level – Special Reserve (Burgundy Bottle Shape)
Varietals: Pinot Noir, Chardonnay, Syrah.
The label must include the mention "Special Reserve."
Premium Level – Limited (Heavy Conical Bottle Shape)
Varietal: Carménère-Malbec.
The label must include the mention "Limited."
Top Level – Secret Blend (Heavy Conical Bottle Shape)
Name on the label: "Secret Blend."
General Label Guidelines
Year: Only mention "2024" (do not include the word “vintage”).
Capsules: Use standard-colored capsules only (no branding).
Design Concept: The style should align with our brand identity. Please refer to www.malvorin-vins.example for inspiration and coherence.

Target Market(s)

younger generation,

Industry/Entity Type

Wines producer

Requirements
Must have
• the original logo with the name it is register We need to indicate the varietals Cabernet Sauvignon, the vintage 2024, the region DO Central Valley
Nice to have
• one white wines version of the label on a burgendy bottle shape and one red wines label on bordeau bottles sahpe

```html
<!DOCTYPE html>
<html lang="en">
<head>
<meta charset="utf-8">
<title>Campo Dormido – Cabernet Sauvignon Label</title>
<link rel="stylesheet" href="https://fonts.googleapis.com/css2?family=EB+Garamond:wght@400;500&display=swap">
<style>
  :root {
    --page-bg: #ffffff;
    --band-green: #1f3428;
    --band-dark: #262626;
    --band-dark-deep: #1b1b1b;
    --cream: #ece7d8;
    --cream-soft: #ddd7c6;
    --mist: #b9b9ad;
    --peak-green: #24372c;
    --peak-deep: #17251d;
    --peak-earth: #6f604a;
  }
  * { margin: 0; padding: 0; box-sizing: border-box; }
  html, body {
    width: 1200px;
    height: 1200px;
    overflow: hidden;
    background: var(--page-bg);
  }
  .canvas {
    position: relative;
    width: 1200px;
    height: 1200px;
    display: flex;
    align-items: center;
    justify-content: center;
  }
  .label {
    width: 880px;
    height: 1010px;
    display: flex;
    flex-direction: column;
    font-family: "EB Garamond", Georgia, serif;
    color: var(--cream);
  }
  .varietal-band {
    height: 121px;
    background: var(--band-green);
    display: flex;
    align-items: center;
    justify-content: center;
    padding-top: 10px;
  }
  .varietal-name {
    font-size: 30px;
    font-weight: 400;
    letter-spacing: 0.36em;
    margin-right: -0.36em;
    text-transform: uppercase;
  }
  .artwork {
    height: 655px;
    background:
      radial-gradient(ellipse 70% 45% at 45% 30%, rgba(36, 55, 44, 0.55) 0%, rgba(36, 55, 44, 0) 70%),
      linear-gradient(180deg,
        var(--cream) 0%,
        var(--cream-soft) 18%,
        var(--mist) 36%,
        var(--peak-green) 58%,
        var(--peak-deep) 72%,
        var(--peak-green) 84%,
        var(--peak-earth) 100%);
  }
  .brand-band {
    flex: 1;
    background: linear-gradient(180deg, var(--band-dark) 0%, var(--band-dark-deep) 100%);
    display: flex;
    align-items: center;
    justify-content: space-between;
    padding: 0 68px 0 60px;
  }
  .brand {
    display: flex;
    align-items: flex-start;
    gap: 16px;
  }
  .brand-name {
    font-size: 50px;
    font-weight: 400;
    line-height: 1.05;
    letter-spacing: 0.04em;
    text-transform: uppercase;
  }
  .brand-name span { display: block; }
  .brand-name span + span { padding-left: 40px; }
  .brand-dot {
    width: 22px;
    height: 22px;
    border-radius: 50%;
    background: var(--cream);
    margin-top: 6px;
  }
  .wine-details {
    text-align: right;
    font-size: 28px;
    line-height: 1.75;
    font-weight: 400;
  }
</style>
</head>
<body>
  <main class="canvas">
    <article class="label">
      <header class="varietal-band">
        <h1 class="varietal-name">Cabernet Sauvignon</h1>
      </header>
      <div class="artwork" role="img" aria-label="Illustration of misty, snow-capped Andes peaks in cream and deep green beneath a dark sun"></div>
      <footer class="brand-band">
        <div class="brand">
          <p class="brand-name"><span>Campo</span><span>Dormido</span></p>
          <div class="brand-dot" aria-hidden="true"></div>
        </div>
        <div class="wine-details">
          <p class="year">2024</p>
          <p class="region">DO Central Valley</p>
        </div>
      </footer>
    </article>
  </main>
</body>
</html>
```